Personal Finance Author needs a postcard

Hi there,

I am a Canadian personal finance author and have published a new book called The Wealth Compass.

I teach Millennials how to create a 6-figure portfolio through investing (https://www.dariafelt.com/)

I'm speaking at some conferences so we were going to print some postcards to hand out to attendees with our info and calls-to-action on them.

I am looking for 4x6 (horizontal) postcard (no space needed for shipping label).

Logos, Headshots and Book Cover:
https://files.cloudvaultex.com/folders/8kQpZrT2mWvN4xLbJ7sHdYc3FgA9eUoRi?usp=sharing

Both sides will be full colour. I would like a clean and simple look. Our main sites are www.DariaFelt.com and www.TheWealthCompassBook.com if you want to get a sense of style and design.
I also uploaded a few marketing materials so you can see the existing designs.

Side 1:
Get Instant Access to your Free Resources - main headline

(small bullets underneath)
- The Wealth Compass Checklist
- Financial Worksheets
- Database of Investment Tools

DariaFelt.com/Resources

At the bottom, include "Don't forget to follow Daria Felt on social media:
Linkedin: @dariafelt7
Facebook: @thewealthcompassbook Instagram: @thewealthcompassbook Twitter: @WealthCompassBk"

Side 2:
Headline - Want to work directly with Daria and The Wealth Compass team to help you make your money grow and stay safe?

Work with us to (bullet point list)...
- Hire Daria as a Keynote Speaker
- Teach Financial Literacy Workshops
- Receive Financial Coaching

Want To Learn More About How We Can Help?
DariaFelt.com/Services

Include my contact info:
Daria Felt
Author | Speaker | Investor
daria@thewealthcompassbook.com
416-555-0187

Target Market(s)

Millennials who want to learn how to save and invest their money. I focus on stock market investing, real estate investing and entrepreneurship.

Industry/Entity Type

Financial Service

Font styles to use
Sans Serif

Colors

Designer to choose colors to be used in the design.

Requirements
Must have
• Photo of Daria Felt
• The Wealth Compass logo
• Green, Gold/Yellow to match existing colours
• modern business style postcard

```html
<!DOCTYPE html>
<html lang="en">
<head>
<meta charset="utf-8">
<title>Daria Felt – Services Postcard</title>
<link href="https://fonts.googleapis.com/css2?family=League+Gothic&display=swap" rel="stylesheet">
<style>
  :root {
    --ink: #111111;
    --gold: #e9b12f;
    --band-gold: #ecb234;
    --green: #0b6130;
    --paper-top: #ececec;
    --paper-bottom: #ffffff;
    --white: #ffffff;
    --rule: #9a9a9a;
  }
  * { margin: 0; padding: 0; box-sizing: border-box; }
  html, body { width: 1200px; height: 800px; overflow: hidden; }
  body {
    font-family: "League Gothic", "Arial Narrow", sans-serif;
    font-weight: 400;
    text-transform: uppercase;
    color: var(--ink);
    letter-spacing: 0.5px;
  }
  .postcard {
    position: relative;
    width: 1200px;
    height: 800px;
    overflow: hidden;
    background: radial-gradient(ellipse at 45% 40%, var(--paper-bottom) 0%, var(--paper-top) 95%);
  }
  .headline {
    position: absolute;
    left: 65px;
    top: 58px;
    width: 850px;
    font-size: 62px;
    line-height: 53px;
    font-weight: 400;
    white-space: nowrap;
  }
  .headline em { color: var(--gold); font-style: italic; }
  .brand-mark {
    position: absolute;
    left: 945px;
    top: 60px;
    width: 200px;
    text-align: center;
    color: var(--green);
    font-size: 72px;
    line-height: 68px;
  }
  .intro {
    position: absolute;
    left: 65px;
    top: 250px;
    font-size: 38px;
  }
  .services {
    position: absolute;
    left: 65px;
    top: 298px;
    display: flex;
    list-style: none;
    color: var(--green);
    font-size: 40px;
    line-height: 35px;
  }
  .services li { white-space: nowrap; }
  .services li:nth-child(1) { width: 248px; }
  .services li:nth-child(2) { width: 334px; }
  .services li + li { border-left: 2px solid var(--green); padding-left: 38px; }
  .cta {
    position: absolute;
    left: 65px;
    top: 408px;
    font-size: 40px;
  }
  .cta-url {
    position: absolute;
    left: 64px;
    top: 459px;
    width: 517px;
    height: 80px;
    border: 2px solid var(--rule);
    display: flex;
    align-items: center;
    justify-content: center;
    font-size: 56px;
    letter-spacing: 2.5px;
  }
  .band-gold {
    position: absolute;
    left: 0; top: 587px;
    width: 1200px; height: 110px;
    background: var(--band-gold);
    display: flex;
    align-items: center;
    padding-left: 65px;
    color: var(--white);
  }
  .name { font-size: 60px; font-style: italic; margin-right: 34px; letter-spacing: 1px; }
  .roles { font-size: 36px; display: flex; align-items: center; letter-spacing: 1px; }
  .roles span + span { border-left: 1.5px solid var(--white); margin-left: 16px; padding-left: 16px; line-height: 26px; }
  .band-green {
    position: absolute;
    left: 0; top: 697px;
    width: 1200px; height: 103px;
    background: var(--green);
    display: flex;
    align-items: center;
    padding-left: 65px;
    color: var(--white);
    font-size: 48px;
    white-space: nowrap;
  }
  .band-green svg { width: 32px; height: 32px; margin-right: 10px; }
  .contact-divider { width: 2px; height: 32px; background: var(--white); margin: 0 24px; }
  .portrait {
    position: absolute;
    left: 925px;
    top: 300px;
    width: 250px;
    height: 500px;
    background: linear-gradient(180deg, #8a5b3c 0%, #d9aa82 30%, #2a2c36 55%, #1c1d24 100%);
    border-radius: 120px 120px 0 0;
  }
  .calculator {
    position: absolute;
    left: 650px;
    top: 390px;
    width: 93px;
    height: 150px;
    background: linear-gradient(180deg, #f1d98e 0%, #e5bf62 100%);
    border-radius: 6px;
  }
</style>
</head>
<body>
  <main class="postcard">
    <h1 class="headline">
      Want to <em>work directly with Daria</em><br>
      and the Wealth Compass team to help you<br>
      <em>make your money grow and stay safe?</em>
    </h1>

    <div class="brand-mark">The<br>Wealth<br>Compass</div>

    <p class="intro">Work with us to:</p>
    <ul class="services">
      <li>Hire Daria as a<br>Keynote Speaker</li>
      <li>Teach Financial<br>Literacy Workshops</li>
      <li>Receive Financial<br>Coaching</li>
    </ul>

    <p class="cta">Want to learn more about how we can help?</p>
    <div class="cta-url">DariaFelt.com/Services</div>

    <div class="band-gold">
      <span class="name">Daria Felt</span>
      <div class="roles"><span>Author</span><span>Speaker</span><span>Investor</span></div>
    </div>

    <div class="band-green">
      <svg viewBox="0 0 24 24" aria-hidden="true"><path fill="#ffffff" d="M6.6 10.8c1.4 2.8 3.8 5.1 6.6 6.6l2.2-2.2c.3-.3.7-.4 1-.2 1.1.4 2.3.6 3.6.6.6 0 1 .4 1 1V20c0 .6-.4 1-1 1C10.6 21 3 13.4 3 4c0-.6.4-1 1-1h3.5c.6 0 1 .4 1 1 0 1.3.2 2.5.6 3.6.1.3 0 .7-.2 1L6.6 10.8z"/></svg>
      <span>416-555-0187</span>
      <span class="contact-divider"></span>
      <span>daria@thewealthcompassbook.com</span>
    </div>

    <div class="calculator" role="img" aria-label="Gold calculator held up in Daria's hand, its display reading PROFIT"></div>
    <div class="portrait" role="img" aria-label="Photo of Daria Felt smiling in a dark blazer, pointing toward the calculator"></div>
  </main>
</body>
</html>
```